Infographic for Commercial Painting and Flooring Company

We need an Infographic that shows a compelling argument for signing on with Verimbos for a maintenance contract vs a project. The infographic should be easily understood visually so sell the story we have provided. 1) What does the quick view give me? 2) Am I interested in this? 3) Does this bring me any value? 4) Is this “everything I have seen before or something new and different”? Included here is a word document called Maintenance vs Project Notes with the written content and instructions, a logo, and two other marketing pieces they currently use so you can see how their brand is being used. Colors should be on brand. I'd like to get this done ASAP if possible. We do not want this piece to look busy.

I added two images called Sample 1 and Sample 2 to portray the types of infographics we like. Simple and clear. Love the watch with the pie chart built in....a smaller version of that would be great for us based on the notes document I provided.

Target Market(s)

Facilities Manufacturers and owners of manufacturing facilities

Font styles to use
Sans Serif

Colors

Designer to choose colors to be used in the design.

Requirements
Must have
• Simple, clean, tell a clear story
Nice to have
• Iconography, pie chart, Men in hard hat
Should not have
• Too many colors. Stick with the brand colors and maybe a few others. Don't want it too look to busy.

```html
<!DOCTYPE html>
<html lang="en">
<head>
<meta charset="utf-8">
<title>Maintenance Program vs. Project – Verimbos</title>
<link href="https://fonts.googleapis.com/css2?family=Oswald:wght@500;600&family=Arimo:wght@400;700&family=Fira+Sans:wght@400;500;700&display=swap" rel="stylesheet">
<style>
  :root {
    --navy: #1c467f;
    --olive: #b2bb35;
    --olive-pale: #d4d687;
    --sky: #cce8f8;
    --white: #ffffff;
    --ink: #1d1d1d;
    --grey: #c8c8c8;
    --blue-light: #8fb4e3;
    --blue-steel: #6a96c4;
    --blue-mid: #3a6aa6;
    --blue-bright: #3d7cc0;
  }
  * { margin: 0; padding: 0; box-sizing: border-box; }
  html, body { width: 1200px; height: 1200px; overflow: hidden; }
  body { background: var(--sky); position: relative; font-family: "Arimo", Arial, sans-serif; }

  .sheet {
    position: absolute; left: 150px; top: 22px;
    width: 900px; height: 1156px; background: var(--white);
  }
  .sheet > * { position: absolute; }

  .title-band {
    left: 12px; top: 12px; width: 876px; height: 63px; background: var(--navy);
    display: flex; align-items: center; justify-content: center; gap: 18px;
    font-family: "Oswald", sans-serif; font-weight: 600; color: var(--white);
    font-size: 46px; letter-spacing: 0.5px;
  }
  .title-band .vs { font-size: 26px; }

  .hero-banner {
    left: 184px; top: 104px; width: 704px; height: 122px; background: var(--olive);
    clip-path: polygon(38px 0, 100% 0, 100% 100%, 38px 100%, 0 50%);
    text-align: center; padding: 14px 0 0 80px; color: var(--navy);
    font-weight: 700;
  }
  .hero-banner .lead { font-size: 24px; line-height: 30px; }
  .hero-banner .sub { font-size: 20px; color: var(--white); margin-top: 6px; }
  .hero-banner .sub u { text-underline-offset: 5px; text-decoration-thickness: 2px; }

  .worker-illustration {
    left: 16px; top: 82px; width: 157px; height: 302px;
    background: linear-gradient(180deg, #e9edf4 0%, #f3f3f3 50%, #dfe6f0 100%);
    border-radius: 6px;
  }

  .hours-callout {
    left: 12px; top: 384px; width: 384px; height: 115px; background: var(--navy);
    clip-path: polygon(0 0, 344px 0, 100% 50%, 344px 100%, 0 100%);
    color: var(--olive); font-weight: 700; font-size: 19px; line-height: 24px;
    text-align: center; padding: 20px 36px 0 8px;
  }
  .hours-callout strong { color: var(--white); font-size: 24px; }

  .watch-chart { left: 400px; top: 240px; }
  .watch-chart .label { font-family: "Arimo", sans-serif; font-weight: 700; font-size: 14px; fill: var(--ink); }
  .watch-chart .num { fill: var(--navy); }
  .watch-chart .hrs-val { font-weight: 700; font-size: 19px; fill: var(--white); }
  .watch-chart .hrs-unit { font-size: 9px; fill: var(--white); font-weight: 700; }

  .stat-box {
    top: 573px; height: 132px; background: var(--olive);
    border: 2px solid var(--navy); border-radius: 22px;
    text-align: center; font-weight: 700; padding-top: 14px;
  }
  .stat-box h2 { font-size: 24px; color: var(--navy); margin-bottom: 10px; }
  .stat-box p { font-size: 24px; color: var(--white); line-height: 31px; }
  .stat-box p b { color: var(--navy); }
  .stat-projects { left: 22px; width: 419px; }
  .stat-once { left: 476px; width: 397px; }

  .program-band {
    left: 12px; top: 719px; width: 876px; height: 44px; background: var(--olive);
    color: var(--white); font-family: "Oswald", sans-serif; font-weight: 600;
    font-size: 32px; text-align: center; line-height: 44px;
  }

  .team-block {
    left: 12px; top: 771px; width: 876px; height: 151px; background: var(--navy);
    color: var(--white); font-family: "Fira Sans", sans-serif; font-weight: 700;
  }
  .team-block h3 { text-align: center; font-size: 18px; margin-top: 10px; letter-spacing: 0.5px; }
  .values { display: flex; justify-content: space-around; padding: 0 100px; margin-top: 14px; }
  .value { text-align: center; font-size: 20px; width: 180px; }
  .value svg { display: block; margin: 0 auto 8px; }

  .benefits {
    left: 12px; top: 931px; width: 876px; height: 155px; background: var(--olive);
    display: grid; grid-template-columns: 388px 400px; padding: 14px 0 0 62px;
    font-family: "Fira Sans", sans-serif; font-weight: 500; font-size: 15.5px; color: var(--navy);
  }
  .benefits ul { list-style: none; }
  .benefits li { height: 31.5px; }
  .benefits li::before { content: "✓"; margin-right: 8px; }

  .footer {
    left: 12px; top: 1086px; width: 876px; height: 60px; background: var(--navy);
  }
  .footer .tagline {
    position: absolute; left: 0; width: 640px; top: 0; line-height: 60px; text-align: center;
    font-family: "Oswald", sans-serif; font-weight: 500; color: var(--white); font-size: 24px;
  }
  .footer .tagline u { text-underline-offset: 4px; }
  .footer .brand-plate {
    position: absolute; right: 0; top: -8px; width: 206px; height: 68px; background: #f4f4f4;
    clip-path: polygon(32px 0, 100% 0, 100% 100%, 0 100%);
    display: flex; align-items: center; justify-content: flex-end; gap: 8px; padding-right: 16px;
  }
  .brand-mark { width: 16px; height: 16px; background: var(--olive); }
  .brand-name { font-family: "Arimo", sans-serif; font-weight: 700; font-size: 22px; color: var(--navy); }
</style>
</head>
<body>
<main class="sheet">
  <header class="title-band"><span>MAINTENANCE PROGRAM</span><span class="vs">VS.</span><span>PROJECT</span></header>

  <div class="worker-illustration" role="img" aria-label="Illustration of a puzzled worker in a yellow hard hat holding rolled plans, with question marks above"></div>

  <section class="hero-banner">
    <p class="lead">IMAGINE WHAT YOU COULD DO WITH<br>30% MORE TIME EACH YEAR</p>
    <p class="sub">TIME YOU GET BACK BY ONBOARDING <u>ONCE</u></p>
  </section>

  <section class="hours-callout">IT TAKES <strong>30+ HOURS</strong> TO SOURCE AND ONBOARD THE MOST QUALIFIED VENDOR...YIKES!</section>

  <svg class="watch-chart" width="490" height="320" viewBox="0 0 490 320" role="img" aria-label="Stopwatch pie chart of 30 onboarding hours">
    <g transform="translate(239,160)">
      <rect x="-3" y="-122" width="6" height="12" fill="var(--navy)"/>
      <rect x="-12" y="-127" width="24" height="7" rx="2" fill="var(--navy)"/>
      <g transform="rotate(45)">
        <rect x="-4" y="-122" width="8" height="12" fill="var(--navy)"/>
        <circle cx="0" cy="-124" r="11" fill="none" stroke="var(--navy)" stroke-width="1.5"/>
      </g>
      <path d="M0 0 L0 -111 A111 111 0 0 1 82.5 -74.3 Z" fill="var(--grey)"/>
      <path d="M0 0 L82.5 -74.3 A111 111 0 0 1 82.5 74.3 Z" fill="var(--olive)"/>
      <path d="M0 0 L82.5 74.3 A111 111 0 0 1 23.1 108.6 Z" fill="var(--blue-light)"/>
      <path d="M0 0 L23.1 108.6 A111 111 0 0 1 -65.2 89.8 Z" fill="var(--blue-steel)"/>
      <path d="M0 0 L-65.2 89.8 A111 111 0 0 1 -96.1 55.5 Z" fill="var(--blue-mid)"/>
      <path d="M0 0 L-96.1 55.5 A111 111 0 0 1 -105.6 -34.3 Z" fill="var(--blue-bright)"/>
      <path d="M0 0 L-105.6 -34.3 A111 111 0 0 1 -65.2 -89.8 Z" fill="var(--navy)"/>
      <path d="M0 0 L-65.2 -89.8 A111 111 0 0 1 0 -111 Z" fill="var(--olive-pale)"/>
      <g text-anchor="middle">
        <text class="hrs-val" x="40" y="-74">4</text><text class="hrs-unit" x="40" y="-63">hrs</text>
        <text class="hrs-val" x="90" y="-6">7</text><text class="hrs-unit" x="90" y="5">hrs</text>
        <text class="hrs-val" x="52" y="66">3</text><text class="hrs-unit" x="52" y="77">hrs</text>
        <text class="hrs-val" x="-20" y="80">4</text><text class="hrs-unit" x="-20" y="91">hrs</text>
        <text class="hrs-val" x="-70" y="50">2</text><text class="hrs-unit" x="-70" y="61">hrs</text>
        <text class="hrs-val" x="-92" y="2">4</text><text class="hrs-unit" x="-92" y="13">hrs</text>
        <text class="hrs-val" x="-73" y="-51">3</text><text class="hrs-unit" x="-73" y="-40">hrs</text>
        <text class="hrs-val" x="-29" y="-85">3</text><text class="hrs-unit" x="-29" y="-74">hrs</text>
      </g>
    </g>
    <g stroke="var(--navy)" stroke-width="1">
      <line x1="197" y1="32" x2="204" y2="55"/>
      <line x1="302" y1="41" x2="291" y2="62"/>
      <line x1="373" y1="161" x2="350" y2="161"/>
      <line x1="318" y1="268" x2="304" y2="249"/>
      <line x1="208" y1="288" x2="213" y2="268"/>
      <line x1="130" y1="235" x2="147" y2="223"/>
      <line x1="106" y1="164" x2="128" y2="163"/>
      <line x1="132" y1="78" x2="151" y2="93"/>
    </g>
    <g fill="var(--navy)">
      <circle cx="197" cy="32" r="2"/><circle cx="302" cy="41" r="2"/>
      <circle cx="373" cy="161" r="2"/><circle cx="318" cy="268" r="2"/>
      <circle cx="208" cy="288" r="2"/><circle cx="130" cy="235" r="2"/>
      <circle cx="106" cy="164" r="2"/><circle cx="132" cy="78" r="2"/>
    </g>
    <g class="label" text-anchor="middle">
      <text x="139" y="30"><tspan class="num">8.</tspan>On-Boarding</text><text x="141" y="47">Paperwork</text>
      <text x="304" y="39" text-anchor="start"><tspan class="num">1.</tspan>Source Vendors</text>
      <text x="421" y="166"><tspan class="num">2.</tspan>Schedule</text><text x="421" y="183">Walkthrough</text>
      <text x="397" y="278"><tspan class="num">3.</tspan>Review Estimates</text>
      <text x="252" y="311"><tspan class="num">4.</tspan>Clarify scope</text>
      <text x="77" y="246"><tspan class="num">5.</tspan>Present to</text><text x="77" y="263">Decision Maker</text>
      <text x="59" y="170"><tspan class="num">6.</tspan>Negotiate</text><text x="59" y="187">with Vendors</text>
      <text x="85" y="82"><tspan class="num">7.</tspan>Award &amp;</text><text x="85" y="99">Purchasing</text>
    </g>
  </svg>

  <section class="stat-box stat-projects">
    <h2>20 PROJECTS</h2>
    <p><b>600</b> Hours or <b>30%</b> of your<br>time per year...UGH!</p>
  </section>
  <section class="stat-box stat-once">
    <h2>ONBOARD ONCE</h2>
    <p><b>1.5 %</b> of your time for the<br>entire year....FOR REAL!</p>
  </section>

  <div class="program-band">DO IT ONCE WITH A PREVENTIVE MAINTENANCE PROGRAM!</div>

  <section class="team-block">
    <h3>WE BECOME AN EXTENSION OF YOUR TEAM...</h3>
    <div class="values">
      <div class="value">
        <svg width="50" height="50" viewBox="0 0 50 50" fill="none" stroke="var(--olive)" stroke-width="5">
          <path d="M9 20 A17 17 0 0 1 40 16"/><path d="M41 30 A17 17 0 0 1 10 34"/>
          <path d="M40 6 L41 17 L30 17" stroke-width="4"/><path d="M10 44 L9 33 L20 33" stroke-width="4"/>
          <circle cx="25" cy="25" r="6" fill="var(--olive)" stroke="none"/>
        </svg>
        CONSISTENCY
      </div>
      <div class="value">
        <svg width="50" height="50" viewBox="0 0 50 50" fill="none" stroke="var(--olive)" stroke-width="5">
          <circle cx="21" cy="23" r="15"/><path d="M32 34 L45 47" stroke-width="6"/>
          <path d="M12 27 L19 20 L24 25 L38 8" stroke-width="4"/><path d="M31 7 L39 7 L39 15" stroke-width="4"/>
        </svg>
        PREDICTABILITY
      </div>
      <div class="value">
        <svg width="50" height="50" viewBox="0 0 50 50" fill="none" stroke="var(--olive)" stroke-width="4.5">
          <path d="M25 4 L42 10 V24 C42 35 34 42 25 46 C16 42 8 35 8 24 V10 Z"/>
          <path d="M16 24 L23 31 L35 17"/>
        </svg>
        RELIABILITY
      </div>
    </div>
  </section>

  <section class="benefits">
    <ul>
      <li>Adherance to Safety as Our #1 Objective</li>
      <li>Follow <u>Your</u> Scheduling Requirements</li>
      <li>A Single Point of Communication</li>
      <li>Work Order Integration &amp; Tracking</li>
    </ul>
    <ul>
      <li>Rapid Response Time</li>
      <li>A Dedicated Field Team Who Knows Your Facility</li>
      <li>Equal Priority for All Tasks (Big or Small)</li>
      <li>Customized Billing and Future Budget Building</li>
    </ul>
  </section>

  <footer class="footer">
    <p class="tagline">WE OPERATE THE WAY <u>YOU</u> OPERATE!</p>
    <div class="brand-plate"><span class="brand-mark"></span><span class="brand-name">Verimbos</span></div>
  </footer>
</main>
</body>
</html>
```